Electronics Recycling and IT Asset Disposition Flyer and Brochure Design

We need a 2 side A5 Flyer and 4 side A4 folder( brochure) for our electronics waste recycling and IT asset management and disposition business.
Our business provides free electronics waste recycling for companies, schools, learning institutions,councils, IT companies and government sectors. Many people are ignorant of responsible recycling of electronics which could harm our health if not treated properly.
The list of other services attached in the pdf.
We provide an end to end and tailored solution for our customers from collection, logistics, data sanitisation, remarketing and recycling.

The Flyer should create awareness of responsible electronics recycling and drive the audience to contact us or go to our website to learn more about the company and services.A brief list of services should also be included in the flyer.The goal is to get the audience to contact us to enquire more about our services.

The Brochure should include all the above plus provide more details about the company, processes, services,contact details (fb, linkedin,Twitter). The goal is to convert the audience to customers for recycling and provide other services as added services.

The final design for both flyer and brochure should communicate responsible recycling of electronic scrap and tailored solution for every organisation.

The company website is www.kelvora-scrap.com.au based in Australia. We serve clients nationwide.

Target Market(s)

IT companies, Corporate, schools and learning institutions, government sector

Industry/Entity Type

Recycling

Contact Information for Business Card

Name: Darren Okefield
email: darren@kelvora-scrap.com.au
website: www.kelvora-scrap.com.au
mobile: +614 173 60294
Phone: 1300 46 2587

Font styles to use
Serif

Requirements
Must have
• I would like the designs to have more images and icons
Nice to have
Should not have
• none

```html
<!DOCTYPE html>
<html lang="en">
<head>
<meta charset="utf-8">
<title>Kelvora Scrap – Service Offering</title>
<link href="https://fonts.googleapis.com/css2?family=Questrial&family=Didact+Gothic&display=swap" rel="stylesheet">
<style>
  :root{
    --green:#5aa83c;
    --green-light:#7cc04e;
    --green-dark:#2f6b22;
    --forest:#1d3f17;
    --grey:#6b6b6b;
    --grey-dark:#4a4a4a;
    --row-grey:#eeeeee;
    --ink:#333333;
    --page:#ffffff;
    --backdrop:#eef2ec;
  }
  *{box-sizing:border-box;margin:0;padding:0}
  html,body{width:1200px;height:878px;overflow:hidden}
  body{background:var(--backdrop);font-family:"Didact Gothic",sans-serif;color:var(--ink);position:relative}
  .sheet{position:absolute;top:114px;width:570px;height:650px;background:var(--page);box-shadow:0 4px 14px rgba(0,0,0,.18);overflow:hidden}
  .sheet--front{left:20px}
  .sheet--back{left:610px}

  /* front */
  .brand-head{height:58px;display:flex;align-items:center;justify-content:center;gap:8px}
  .brand-dot{width:14px;height:14px;border-radius:50%;background:var(--green)}
  .brand-name{font-family:"Questrial",sans-serif;font-size:20px;color:var(--green)}
  .hero{position:relative;height:170px;background:linear-gradient(135deg,#2d4a25 0%,#4f7d3a 45%,#8fae6a 75%,#3e5e30 100%)}
  .hero-icons{position:absolute;top:58px;left:0;right:0;display:flex;justify-content:center;gap:14px}
  .hero-icon{width:40px;height:40px;border-radius:50%;background:var(--green);border:2px solid #fff;display:flex;align-items:center;justify-content:center}
  .hero-title{position:absolute;bottom:8px;width:100%;text-align:center;font-family:"Questrial",sans-serif;font-size:27px;color:#fff;font-weight:400}
  .lead-bar{height:24px;background:var(--green);color:#fff;font-family:"Questrial",sans-serif;font-size:14px;padding-left:140px;line-height:24px}
  .services{list-style:none}
  .service{display:flex;padding:6px 0}
  .service:nth-child(odd){background:var(--row-grey)}
  .service-icon{width:140px;display:flex;justify-content:center;align-items:flex-start;padding-top:2px}
  .ring{width:30px;height:30px;border-radius:50%;border:2px solid var(--green);background:#fff;display:flex;align-items:center;justify-content:center}
  .service-body{flex:1;padding-right:20px}
  .service-title{font-family:"Questrial",sans-serif;color:var(--green);font-size:12.5px;margin-bottom:2px;font-weight:400}
  .service-text{font-size:7.6px;line-height:1.32}
  .foot-bars{position:absolute;bottom:0;left:0;right:0;height:9px;display:flex}
  .foot-bars span:nth-child(1){flex:1;background:var(--green-light)}
  .foot-bars span:nth-child(2){flex:1.3;background:var(--green-dark)}
  .foot-bars span:nth-child(3){flex:1.3;background:var(--forest)}
  .foot-bars span:nth-child(4){flex:5;background:var(--grey)}

  /* back */
  .cycle{position:absolute;left:10px;top:12px}
  .cycle-note{font-family:"Didact Gothic",sans-serif;font-size:4.4px;line-height:1.3}
  .brand-side{position:absolute;right:40px;top:262px;display:flex;align-items:center;gap:10px}
  .brand-side .brand-dot{width:34px;height:34px;background:none;border:2px solid var(--green)}
  .brand-side p{font-family:"Questrial",sans-serif;color:var(--green);font-size:12px;line-height:1.35}
  .block{position:absolute;left:0;right:0;text-align:center}
  .block-icon{width:28px;height:28px;margin:0 auto;border-radius:50%;background:var(--green);display:flex;align-items:center;justify-content:center}
  .block-title{font-family:"Questrial",sans-serif;color:var(--green);font-size:11.5px;margin:3px 0 4px;font-weight:400}
  .block-text{font-size:7.4px;line-height:1.35;text-align:left;padding:0 40px}
  .logistics{top:342px;height:96px;background:var(--row-grey);padding-top:4px}
  .industries{top:444px}
  .industry-list{list-style:none;text-align:left;padding-left:40px;margin-top:4px;font-size:7.4px;line-height:1.35}
  .industry-list li::before{content:"";display:inline-block;width:4px;height:4px;background:var(--green);margin-right:6px;vertical-align:middle}
  .contact-line{position:absolute;left:50px;right:50px;bottom:16px;display:flex;justify-content:space-between;font-size:8.5px;color:var(--green);border-bottom:1px solid var(--green);padding-bottom:4px}
</style>
</head>
<body>

<section class="sheet sheet--front">
  <header class="brand-head"><span class="brand-dot"></span><span class="brand-name">Kelvora Scrap</span></header>
  <div class="hero" role="img" aria-label="Close-up photograph of a green electronic circuit board with chips and components">
    <div class="hero-icons">
      <span class="hero-icon"><svg width="20" height="20" viewBox="0 0 20 20" fill="none" stroke="#fff" stroke-width="1.6"><path d="M10 3l3 5H7zM4 15l3-5 3 5zM16 15l-3-5 3 0z"/></svg></span>
      <span class="hero-icon"><svg width="20" height="20" viewBox="0 0 20 20" fill="none" stroke="#fff" stroke-width="1.6"><rect x="5" y="3" width="10" height="14"/><path d="M7 7h6M7 10h6M7 13h4"/></svg></span>
      <span class="hero-icon"><svg width="20" height="20" viewBox="0 0 20 20" fill="none" stroke="#fff" stroke-width="1.6"><ellipse cx="10" cy="6" rx="5" ry="2"/><path d="M5 6v8c0 1 2 2 5 2s5-1 5-2V6"/></svg></span>
      <span class="hero-icon"><svg width="20" height="20" viewBox="0 0 20 20" fill="none" stroke="#fff" stroke-width="1.6"><path d="M4 10a6 6 0 0110-4M16 10a6 6 0 01-10 4"/><path d="M14 3v3h-3M6 17v-3h3"/></svg></span>
      <span class="hero-icon"><svg width="20" height="20" viewBox="0 0 20 20" fill="none" stroke="#fff" stroke-width="1.8"><path d="M4 4l12 12M16 4L4 16"/></svg></span>
      <span class="hero-icon"><svg width="20" height="20" viewBox="0 0 20 20" fill="none" stroke="#fff" stroke-width="1.6"><circle cx="10" cy="10" r="6"/><path d="M8 7l5 3-5 3z" fill="#fff"/></svg></span>
    </div>
    <h1 class="hero-title">Service Offering</h1>
  </div>
  <div class="lead-bar">Secure E-Waste Collection Service</div>
  <ul class="services">
    <li class="service">
      <div class="service-icon"><span class="ring"><svg width="14" height="14" viewBox="0 0 20 20" fill="none" stroke="#5aa83c" stroke-width="2"><path d="M10 3l3 5H7zM4 15l3-5 3 5zM16 15l-3-5 3 0z"/></svg></span></div>
      <div class="service-body"><p class="service-text">Kelvora Scrap collects electronic waste from schools, businesses, home users and government departments<br>Secure collection includes pick up of e-waste and transportation to our recycling facility in a secured truck<br>Registration of assets and reporting</p></div>
    </li>
    <li class="service">
      <div class="service-icon"><span class="ring"><svg width="14" height="14" viewBox="0 0 20 20" fill="none" stroke="#5aa83c" stroke-width="2"><rect x="5" y="3" width="10" height="14"/><path d="M7 8h6M7 12h6"/></svg></span></div>
      <div class="service-body"><h2 class="service-title">Receipting Registration, Test and Audit Services</h2><p class="service-text">Registering your assets on our Asset Management System<br>Test, audit and verify specifications, condition and resale value. Provide a detailed asset report<br>Cleaning and removal of company logos and asset tags</p></div>
    </li>
    <li class="service">
      <div class="service-icon"><span class="ring"><svg width="14" height="14" viewBox="0 0 20 20" fill="none" stroke="#5aa83c" stroke-width="2"><ellipse cx="10" cy="6" rx="5" ry="2"/><path d="M5 6v8c0 1 2 2 5 2s5-1 5-2V6"/></svg></span></div>
      <div class="service-body"><h2 class="service-title">Certified Data Erasure Services</h2><p class="service-text">To provide secure data destruction:<br>X1 pass<br>X3 pass (Recommended, MilSec standard)<br>X7 pass<br>Total destruction of HDDs by degaussing<br>Total physical destruction of any storage media by shredding</p></div>
    </li>
    <li class="service">
      <div class="service-icon"><span class="ring"><svg width="14" height="14" viewBox="0 0 20 20" fill="none" stroke="#5aa83c" stroke-width="2"><path d="M4 10a6 6 0 0110-4M16 10a6 6 0 01-10 4"/></svg></span></div>
      <div class="service-body"><h2 class="service-title">IT Asset Remarketing</h2><p class="service-text">Recover client's IT asset and mobile devices for valuation and remarketing</p></div>
    </li>
    <li class="service">
      <div class="service-icon"><span class="ring"><svg width="14" height="14" viewBox="0 0 20 20" fill="none" stroke="#5aa83c" stroke-width="2.2"><path d="M4 4l12 12M16 4L4 16"/></svg></span></div>
      <div class="service-body"><h2 class="service-title">Processing &amp; recycling of electronic waste</h2><p class="service-text">All assets with no market value will be processed as E-Waste and recycled with zero to landfill<br>in our ISO certified partner refinery overseas for metals recovery</p></div>
    </li>
    <li class="service">
      <div class="service-icon"><span class="ring"><svg width="14" height="14" viewBox="0 0 20 20" fill="none" stroke="#5aa83c" stroke-width="2"><circle cx="10" cy="10" r="6"/><path d="M8 7l5 3-5 3z" fill="#5aa83c"/></svg></span></div>
      <div class="service-body"><h2 class="service-title">IT Services &amp; Data Center Setup, Relocation and Decommissioning</h2><p class="service-text">Deployment, relocation and decommissioning of IT systems by professional Norvane and Trelix certified engineers<br>Data Center decommissioning/racking/de-racking and relocation<br>IT Systems deployment and support for small and medium size business</p></div>
    </li>
    <li class="service">
      <div class="service-icon"></div>
      <div class="service-body"><h2 class="service-title">IT Asset Auditing</h2><p class="service-text">Recording of Manufacturer and Model per asset (additionally HDD quantity and capacity for Server &amp; Storage assets)</p></div>
    </li>
  </ul>
  <div class="foot-bars"><span></span><span></span><span></span><span></span></div>
</section>

<section class="sheet sheet--back">
  <svg class="cycle" width="300" height="300" viewBox="0 0 300 300">
    <circle cx="150" cy="150" r="100" fill="none" stroke="#5aa83c" stroke-width="76" stroke-dasharray="200 428" transform="rotate(-200 150 150)"/>
    <circle cx="150" cy="150" r="100" fill="none" stroke="#dfe9d6" stroke-width="76" stroke-dasharray="200 428" transform="rotate(-80 150 150)"/>
    <circle cx="150" cy="150" r="100" fill="none" stroke="#6b6b6b" stroke-width="76" stroke-dasharray="200 428" transform="rotate(40 150 150)"/>
    <circle cx="150" cy="150" r="56" fill="#fff" stroke="#e3e3e3" stroke-width="4"/>
    <text x="150" y="146" text-anchor="middle" font-family="Questrial, sans-serif" font-size="15" fill="#333">E-waste</text>
    <text x="150" y="166" text-anchor="middle" font-family="Questrial, sans-serif" font-size="15" fill="#333">Recycling</text>

    <text x="104" y="58" font-family="Questrial, sans-serif" font-size="26" fill="#fff">01</text>
    <text x="40" y="84" font-family="Questrial, sans-serif" font-size="8" fill="#fff">REUSE</text>
    <foreignObject x="30" y="90" width="58" height="80"><p xmlns="http://www.w3.org/1999/xhtml" class="cycle-note" style="color:#fff">Reuse: the first step is to visually inspect all defects and identify the usability and functionality to determine the value of each device. Devices with resale value will be sorted and logged for further testing and refurbishing work.</p></foreignObject>

    <text x="214" y="98" font-family="Questrial, sans-serif" font-size="8" fill="#4a4a4a">RECOVER</text>
    <foreignObject x="214" y="103" width="56" height="40"><p xmlns="http://www.w3.org/1999/xhtml" class="cycle-note" style="color:#4a4a4a">Recover: the device that does not pass the initial visual inspection will be segregated and sorted for dismantling process.</p></foreignObject>
    <text x="226" y="192" font-family="Questrial, sans-serif" font-size="26" fill="#4a4a4a">02</text>

    <text x="58" y="224" font-family="Questrial, sans-serif" font-size="26" fill="#fff">03</text>
    <text x="104" y="230" font-family="Questrial, sans-serif" font-size="8" fill="#fff">RECYCLE</text>
    <foreignObject x="104" y="234" width="84" height="40"><p xmlns="http://www.w3.org/1999/xhtml" class="cycle-note" style="color:#fff">Recycle: all dismantled components and materials are sent to downstream vendors for further refining and to be used as raw material for new products.</p></foreignObject>
  </svg>
  <div class="brand-side"><span class="brand-dot"></span><p>Kelvora Scrap<br>E-waste<br>Recycling</p></div>

  <div class="block logistics">
    <div class="block-icon"><svg width="16" height="16" viewBox="0 0 20 20" fill="#fff"><rect x="2" y="6" width="10" height="7"/><path d="M12 8h4l2 3v2h-6z"/><circle cx="6" cy="15" r="1.6"/><circle cx="15" cy="15" r="1.6"/></svg></div>
    <h3 class="block-title">Logistics</h3>
    <p class="block-text">We manage the collection and sorting of equipment carefully so that they are not damaged during the process of loading and transportation. This is to ensure any refurbishable or working device does not lose its value due to the way it is handled and transported to our recycling facility. Each device is manually handled and sorted according to its type and condition by our trained collection team.</p>
  </div>

  <div class="block industries">
    <div class="block-icon"><svg width="16" height="16" viewBox="0 0 20 20" fill="#fff"><rect x="4" y="4" width="12" height="13"/><rect x="7" y="7" width="2" height="2" fill="#5aa83c"/><rect x="11" y="7" width="2" height="2" fill="#5aa83c"/><rect x="7" y="11" width="2" height="2" fill="#5aa83c"/><rect x="11" y="11" width="2" height="2" fill="#5aa83c"/></svg></div>
    <h3 class="block-title">Industries Served</h3>
    <p class="block-text">No matter how big or small your organisation is or how complex or simple your IT systems are, we listen to the needs of your organisation to deliver customized, cost-effective and scalable solution. We ensure data destruction and responsible recycling of your electronic assets are our utmost priority. Our dedicated team is ready to serve you.</p>
    <ul class="industry-list">
      <li>Industries we serve:</li>
      <li>Corporate</li>
      <li>IT Companies</li>
      <li>Financial Institutions</li>
      <li>Educational &amp; Learning Institutions</li>
      <li>Councils</li>
      <li>Recycling companies</li>
      <li>Government sector</li>
    </ul>
  </div>

  <div class="contact-line"><span>18-22 Ridgeline Road, Arndell Park 2148 NSW</span><span>1300 46 2587</span><span>www.kelvora-scrap.com.au</span></div>
  <div class="foot-bars"><span></span><span></span><span></span><span></span></div>
</section>

</body>
</html>
```